gka 2014 bcard design

We have a new logo that we have yet to incorporate into any of our materials. We are under the gun to get new business cards done as soon as possible. This is our 20th year in business and we specialize in providing entertainment and audio-visual services for private and corporate events. Please see our website for more www.goldkiteacts.com
Being that we're in the entertainment industry, our "look" can be somewhat edgy and risky, but at the same time not "over the top". In fact, we would probably lean to a "less is more" style.
One side of the card should have our contact information for phones, email and address, and the other should have our slogan "celebrate, motivate, fascinate". We also want Facebook and Instagram (goldkiteactsevents) there as well, but not sure if it should be on back or front.
Target Market(s)
High net worth individuals, creative types in both the corporate and social markets
Industry/Entity Type
Entertainment
Look and feel

```html
<!DOCTYPE html>
<html lang="en">
<head>
<meta charset="utf-8">
<title>gka business card</title>
<link rel="stylesheet" href="https://fonts.googleapis.com/css2?family=Quicksand:wght@400;500;600;700&display=swap">
<style>
  :root {
    --ink: #231f20;
    --accent: #f7941d;
    --card-white: #ffffff;
    --grey-light: #e6e6e6;
    --grey-mid: #a3a3a3;
    --grey-dark: #6d6d6d;
    --stage: #d9d9d9;
  }
  * { margin: 0; padding: 0; box-sizing: border-box; }
  html, body {
    width: 1200px; height: 1028px; overflow: hidden;
    background: var(--stage);
    font-family: "Quicksand", sans-serif;
    color: var(--ink);
  }
  .card {
    position: absolute; top: 55px; height: 910px;
    border: 1px solid #bdbdbd;
  }
  .card--front {
    left: 27px; width: 563px;
    background: radial-gradient(ellipse 70% 55% at 50% 50%, var(--grey-light) 0%, var(--grey-mid) 55%, var(--grey-dark) 100%);
  }
  .card--back { left: 625px; width: 547px; background: var(--card-white); }

  .brand-dot {
    position: absolute; border: 14px solid var(--accent); border-radius: 50%;
  }
  .brand-name {
    position: absolute; left: 0; width: 100%; text-align: center;
    font-weight: 500; color: var(--ink); letter-spacing: -1px; line-height: 1;
  }
  .brand-tagline {
    position: absolute; left: 0; width: 100%; text-align: center;
    font-weight: 500; letter-spacing: 6px; line-height: 1;
  }
  .slogan {
    position: absolute; left: 0; width: 100%; top: 640px; text-align: center;
    font-size: 22px; font-weight: 600; letter-spacing: 3px; color: #2b2b2b;
  }
  .website {
    position: absolute; left: 0; width: 100%; top: 833px; text-align: center;
    font-size: 30px; font-weight: 700; letter-spacing: 6px; color: #2b2b2b;
  }

  .person-dot {
    position: absolute; left: 40px; top: 434px; width: 30px; height: 30px;
    border: 4px solid var(--accent); border-radius: 50%;
  }
  .person-name {
    position: absolute; left: 82px; top: 428px;
    font-size: 30px; font-weight: 700; color: var(--accent);
  }
  .person-role { position: absolute; left: 82px; top: 464px; font-size: 19px; font-weight: 600; }

  .info-row {
    position: absolute; left: 250px; display: flex; align-items: center; gap: 14px;
    font-size: 19px; font-weight: 500; letter-spacing: 1px; line-height: 24px;
  }
  .info-icon {
    width: 22px; height: 22px; background: var(--accent); border-radius: 4px;
    display: flex; align-items: center; justify-content: center; flex: none;
  }
  .section-title { position: absolute; font-size: 23px; font-weight: 700; }
  .section-title .highlight { color: var(--accent); }
  .address {
    position: absolute; left: 118px; top: 656px;
    font-size: 19px; font-weight: 500; letter-spacing: 1px; line-height: 25px;
  }
  .faint-circle {
    position: absolute; left: 10px; top: 712px; width: 180px; height: 180px;
    border: 16px solid var(--accent); border-radius: 50%; opacity: 0.18;
  }
</style>
</head>
<body>

<section class="card card--front">
  <div class="brand-dot" style="left:186px; top:163px; width:200px; height:200px;"></div>
  <div class="brand-name" style="top:372px; font-size:60px;">gold kite acts</div>
  <div class="brand-tagline" style="top:446px; font-size:30px;">EVENTS &amp;</div>
  <div class="brand-tagline" style="top:486px; font-size:30px;">ENTERTAINMENT</div>
  <div class="slogan">celebrate, motivate, fascinate</div>
  <div class="website">www.goldkiteacts.com</div>
</section>

<section class="card card--back">
  <div class="brand-dot" style="left:176px; top:30px; width:200px; height:200px;"></div>
  <div class="brand-name" style="top:240px; font-size:60px;">gold kite acts</div>
  <div class="brand-tagline" style="top:312px; font-size:30px;">EVENTS &amp;</div>
  <div class="brand-tagline" style="top:352px; font-size:30px;">ENTERTAINMENT</div>

  <div class="person-dot"></div>
  <div class="person-name">Marcus Delaney</div>
  <div class="person-role">Director</div>

  <div class="info-row" style="top:506px;">
    <span class="info-icon">
      <svg width="16" height="16" viewBox="0 0 16 16"><path d="M4 1.5 6 4.5 4.8 6c.8 2 2.2 3.4 4.2 4.2L10.5 9l3 2-1.2 2.5C7 13.5 2.5 9 2.5 3.7z" fill="#fff"/></svg>
    </span>
    <span>555-014-2286</span>
  </div>
  <div class="info-row" style="top:541px;">
    <span class="info-icon">
      <svg width="16" height="12" viewBox="0 0 18 14"><rect x="1" y="1" width="16" height="12" fill="none" stroke="#fff" stroke-width="1.8"/><path d="M1 1 9 8 17 1" fill="none" stroke="#fff" stroke-width="1.8"/></svg>
    </span>
    <span>info@goldkiteactsevents</span>
  </div>

  <div class="section-title" style="left:82px; top:624px;"><span class="highlight">GoldKiteActs</span> company:</div>
  <div class="address">48 Harlow Avenue, 3rd Floor<br>Brookfield, NY 10020</div>

  <div class="faint-circle"></div>

  <div class="section-title" style="left:225px; top:748px;">Follow us on:</div>
  <div class="info-row" style="top:789px;">
    <span class="info-icon">
      <svg width="14" height="14" viewBox="0 0 14 14"><circle cx="3" cy="7" r="2" fill="#fff"/><circle cx="11" cy="3" r="2" fill="#fff"/><circle cx="11" cy="11" r="2" fill="#fff"/><path d="M3 7 11 3M3 7l8 4" stroke="#fff" stroke-width="1.4"/></svg>
    </span>
    <span>/goldkiteactsevents</span>
  </div>
  <div class="info-row" style="top:814px;">
    <span class="info-icon">
      <svg width="14" height="14" viewBox="0 0 14 14"><path d="M2 2h10v7H6l-3 3V9H2z" fill="#fff"/></svg>
    </span>
    <span>/goldkiteactsevents</span>
  </div>
  <div class="info-row" style="top:839px;">
    <span class="info-icon">
      <svg width="14" height="14" viewBox="0 0 14 14"><path d="M7 1.5l1.7 3.5 3.8.5-2.8 2.6.7 3.8L7 10.1 3.6 11.9l.7-3.8L1.5 5.5l3.8-.5z" fill="#fff"/></svg>
    </span>
    <span>/goldkiteactsevents</span>
  </div>
</section>

</body>
</html>
```